Irrigation Business needs their business cards modernised and revamped

I would like to keep my current logo, colours and revamp the format of the card.

I would like the card to be clean yet important.

Im not sure if you include texture but i would like the named logo to be indented into the card etc.

show me something alive and free something thats clinical to the point yet has a feel of achievement. i would like people to go nice card.

Target Market(s)

high end clients, corporate, sports field manger, the guys that make the decisions

Industry/Entity Type

Business

Contact Information for Business Card

nformation to be included

Dorian Hesk (Director)
0487253916
dorian@tfcraft.biz
www.taddsfieldcrafts.com

instagram logo
google logo
facebook logo

Colors

Designer to choose colors to be used in the design.

Requirements
Nice to have
• indentations a really nice feel to the card good texture

```html
<!DOCTYPE html>
<html lang="en">
<head>
<meta charset="utf-8">
<title>Tadd's Field Crafts — Business Card</title>
<link href="https://fonts.googleapis.com/css2?family=Roboto:wght@400;500;700&family=Roboto+Condensed:wght@700&display=swap" rel="stylesheet">
<style>
  :root {
    --backdrop: #2b2b2b;
    --card-white: #f1f1f1;
    --brand-blue: #2f64a6;
    --brand-green: #3fa46a;
    --back-blue: #3d6cab;
    --back-blue-light: #4676b4;
    --text-grey: #4a4a4a;
    --white: #ffffff;
  }
  * { margin: 0; padding: 0; box-sizing: border-box; }
  html, body { width: 1200px; height: 960px; overflow: hidden; }
  body {
    background: var(--backdrop);
    font-family: "Roboto", Arial, sans-serif;
    position: relative;
  }
  .card {
    position: absolute;
    width: 600px;
    height: 343px;
    overflow: hidden;
  }
  /* Front */
  .card--front { left: 314px; top: 113px; background: var(--card-white); }
  .band {
    position: absolute; top: 47px; height: 80px; left: 0; width: 446px;
    background: var(--brand-blue);
  }
  .band--accent { left: 446px; width: 154px; background: var(--brand-green); }
  .holder { position: absolute; left: 47px; top: 66px; color: var(--white); }
  .holder__name {
    font-family: "Roboto Condensed", "Arial Narrow", sans-serif;
    font-weight: 700; font-size: 21px; letter-spacing: 0.2px;
  }
  .holder__title { font-size: 14px; font-weight: 500; margin-top: 2px; letter-spacing: 0.3px; }
  .brand-mark {
    position: absolute; left: 404px; top: 45px; width: 84px; height: 84px;
    border-radius: 50%; background: var(--brand-blue); border: 3px solid var(--white);
  }
  .brand-name {
    position: absolute; left: 300px; width: 292px; top: 133px; text-align: center;
    color: var(--brand-blue); font-weight: 700; font-size: 22px; letter-spacing: 0.2px;
  }
  .contacts { position: absolute; left: 48px; top: 245px; list-style: none; }
  .contacts li {
    display: flex; align-items: center; height: 19px;
    font-size: 14px; color: var(--text-grey);
  }
  .contacts svg { width: 13px; height: 13px; margin-right: 8px; fill: var(--brand-blue); }
  /* Back */
  .card--back {
    left: 311px; top: 472px;
    background: linear-gradient(135deg, var(--back-blue-light), var(--back-blue));
  }
  .back-ring {
    position: absolute; left: 263px; top: 10px; width: 326px; height: 326px;
    border-radius: 50%; border: 10px solid rgba(255,255,255,0.1);
  }
  .back-name {
    position: absolute; left: 18px; width: 240px; top: 236px; text-align: center;
    color: var(--white); font-weight: 700; font-size: 21px;
  }
  .social {
    position: absolute; left: 36px; top: 287px; width: 200px;
    display: flex; align-items: center; justify-content: center; gap: 4px;
  }
  .social__rule { width: 54px; height: 1px; background: rgba(255,255,255,0.5); margin: 0 2px; }
  .social__dot { width: 28px; height: 28px; border-radius: 50%; background: var(--white); }
</style>
</head>
<body>
  <section class="card card--front">
    <div class="band"></div>
    <div class="band band--accent"></div>
    <div class="holder">
      <p class="holder__name">DORIAN HESK</p>
      <p class="holder__title">DIRECTOR</p>
    </div>
    <div class="brand-mark"></div>
    <p class="brand-name">TADD'S FIELD CRAFTS</p>
    <ul class="contacts">
      <li><svg viewBox="0 0 24 24"><path d="M6.6 10.8a15.2 15.2 0 0 0 6.6 6.6l2.2-2.2a1 1 0 0 1 1-.25 11.4 11.4 0 0 0 3.6.57 1 1 0 0 1 1 1V20a1 1 0 0 1-1 1A17 17 0 0 1 3 4a1 1 0 0 1 1-1h3.5a1 1 0 0 1 1 1c0 1.25.2 2.45.57 3.57a1 1 0 0 1-.25 1z"/></svg>0487253916</li>
      <li><svg viewBox="0 0 24 24"><path d="M2 5h20v14H2z M2 5l10 8 10-8" /></svg>dorian@tfcraft.biz</li>
      <li><svg viewBox="0 0 24 24"><circle cx="12" cy="12" r="10"/></svg>taddsfieldcrafts.com</li>
    </ul>
  </section>

  <section class="card card--back">
    <div class="back-ring"></div>
    <p class="back-name">TADD'S FIELD CRAFTS</p>
    <div class="social">
      <span class="social__rule"></span>
      <span class="social__dot"></span>
      <span class="social__dot"></span>
      <span class="social__dot"></span>
      <span class="social__rule"></span>
    </div>
  </section>
</body>
</html>
```